WordPress Direct-Booking Website for Bend, Oregon Vacation Rental — $750 Budget
Project Overview

We are looking for a talented WordPress designer/developer to create a clean, professional and inviting direct-booking website for Cedar Lantern Retreat, an established short-term vacation rental in Bend, Oregon.

The property is currently successfully listed on Staynest and Lodgr. Our Staynest property has approximately a 4.98-star rating with more than 200 reviews, is an Staynest Guest Pick, and ranks among the Top 1% of eligible homes.

Project Budget: $750

We will select the designer based on the quality of the initial concept, understanding of the property, proposed booking solution and ability to deliver a completed and functioning WordPress website.

Existing Staynest Listing

Please use our current Staynest listing as the primary reference for photographs, property details, amenities and design inspiration:

https://www.staynest.example/rooms/48170356

Original high-resolution photographs and additional property information will be provided to the selected designer.

Design Direction

We want the website to feel:

Upscale but comfortable
Warm and welcoming
Clean and uncluttered
Pacific Northwest / Central Oregon
Professional rather than corporate
Highly visual with large property photographs
Easy to navigate
Excellent on phones, tablets and desktop computers

We welcome creativity and want designers to show us their vision for the property rather than simply copying our Staynest listing.

The website should immediately communicate that Cedar Lantern Retreat is a highly rated vacation rental in an excellent Bend location.

Key Property Features
3 bedrooms
2 bathrooms
Sleeps up to 6 guests
Pet friendly
Approximately a 5-minute walk to Bend's Tanager Quarter
Near restaurants, shopping and Brightwater Lawn Pavilion
Private fenced backyard
Covered outdoor area
Off-street driveway parking
Fireplace
Well-equipped kitchen
Staynest Premier Host
Staynest Guest Pick
Top 1% of eligible Staynest homes
Approximately 4.98 stars with 200+ guest reviews

Our location, guest reviews, cleanliness, comfort, backyard, pet-friendly accommodations and walkability should be major selling points throughout the website.

Website Structure

We anticipate approximately 6–7 pages:

Home

Large hero photograph with a strong opening message and prominent BOOK DIRECT and CHECK AVAILABILITY buttons.

The home page should quickly communicate:

CEDAR LANTERN RETREAT — BEND, OREGON

3 Bedrooms | 2 Baths | Sleeps 6 | Pet Friendly | Walk to Tanager

Our exceptional guest rating and Staynest history should also be prominently featured.

The House

Bedrooms, bathrooms, kitchen, living areas, backyard and major amenities.

Photo Gallery

Large, attractive and fast-loading photographs with an easy-to-use mobile gallery.

Location / Explore Bend

Tanager Quarter, Brightwater Lawn Pavilion, Kettleback River, restaurants, breweries, shopping, downtown Bend and nearby outdoor recreation.

Guest Reviews

Selected guest reviews and prominent presentation of our strong Staynest reputation.

Availability & Book Direct

A simple and professional direct-booking experience.

Contact / FAQ

Contact information plus common questions regarding pets, parking, check-in/check-out, cancellations and other policies.

IMPORTANT — Direct Booking & Credit Card Requirements

We want guests to be able to book directly through the website without having to contact us first.

The website should use a proven WordPress vacation-rental booking plugin or system rather than a custom-built reservation/payment system.

Guests should be able to:

Select arrival and departure dates
See available dates
Enter number of guests
See nightly charges
See cleaning fees
See applicable lodging taxes and other charges
See the complete reservation total before paying
Enter guest/contact information
Pay securely by credit or debit card
Receive an automatic reservation confirmation

Paywell is our preferred credit-card processor.

Credit-card information must be processed securely through Paywell or another established payment processor. Credit-card information should NOT be stored directly on our WordPress website.

Staynest & Lodgr Calendar Synchronization

This is very important.

The direct-booking calendar must synchronize with our existing Staynest and Lodgr calendars to reduce the possibility of double bookings.

For this single-property website, we prefer a simple solution using Staynest/Lodgr calendar or iCal synchronization rather than an expensive monthly channel-management service, if practical.

The designer should clearly identify the booking plugin/system they propose using.

IMPORTANT — Tell Us Your Proposed Booking Solution

As part of your submission, please tell us:

Which WordPress booking plugin/system you recommend.
Whether it synchronizes availability with Staynest and Lodgr.
Whether it integrates directly with Paywell.
The initial cost of the plugin/software.
Any annual or monthly fees.
Whether any additional paid software or services will be required.

We strongly prefer a solution with little or no ongoing monthly software expense.

We do not want to select a designer and later discover that the proposed booking system requires an expensive monthly subscription.

WordPress & Technical Requirements

The completed project should include:

Fully functioning WordPress website
Responsive desktop/tablet/mobile design
Fast-loading pages
Optimized photographs
SSL/HTTPS compatibility
Direct-booking functionality
Paywell payment integration
Staynest calendar synchronization
Lodgr calendar synchronization
Automatic booking confirmations
Cleaning fee and lodging-tax calculations
Contact form
Wayfind Maps/location integration
Basic spam/security protection
Wayfind Metrics capability
Basic SEO setup
Search-engine submission capability
Easy owner editing of text, rates and photographs
Search Engine Optimization

The website should be structured for Wayfind and other search engines.

Important search themes include:

Bend Oregon vacation rental
Bend Oregon vacation home
Tanager Quarter vacation rental
Vacation rental near Tanager Bend
Bend Oregon pet-friendly vacation rental
Bend vacation rental near Brightwater Lawn Pavilion
Bend Oregon direct booking vacation rental

We are not expecting an extensive ongoing SEO campaign for the $750 project. We do expect proper page titles, descriptions, headings, image optimization and a good technical foundation for future SEO.

Ownership

Upon completion and final payment:

We own the completed WordPress website.
We receive full WordPress administrator access.
We control the domain and hosting accounts.
We own all custom design files created for the project.
All necessary login credentials are provided to us.
The website can be moved to another WordPress hosting provider in the future.
There should be no proprietary dependency on the developer after completion.
What We Want From Contestants

Please review our Staynest listing before submitting your concept.

We are particularly interested in seeing an initial homepage concept showing how you would present:

Cedar Lantern Retreat
The Bend / Tanager location
Our photography
Our exceptional guest reviews and ratings
The Book Direct message
The availability/booking call-to-action

We will provide feedback on the concepts we like and work with the selected designer to refine and complete the website.

Our Goal

Our objective is straightforward:

Create a beautiful, trustworthy and easy-to-use website that encourages guests to book Cedar Lantern Retreat directly with us.

The website will complement—not replace—our existing Staynest and Lodgr listings.

We want repeat guests and new customers to have an easy way to find the property, check availability and book directly while receiving the same professional experience they expect from a major vacation-rental platform.

Target Market(s)

Consumers looking to to travel to Mexico for vacation. Family or couples

Industry/Entity Type

Short term vacation rental industry

Coding

Coded - Design and coding required

Number of Pages Required

5+ page

Requirements
Must have
• Capabilities to accept credit card payments and link to other rental property sites calendars such as LODGR and Staynets
Nice to have
• Option for best plugins for property rental

```html
<!DOCTYPE html>
<html lang="en">
<head>
<meta charset="utf-8">
<title>Cedar Lantern Retreat — Bend, Oregon Vacation Rental</title>
<link rel="stylesheet" href="https://fonts.googleapis.com/css2?family=Playfair+Display:wght@400;500&family=DM+Sans:wght@400;500;700&display=swap">
<style>
:root{
  --forest:#1c3529;
  --forest-2:#23402f;
  --rust:#b85b3d;
  --sand:#f3ede5;
  --cream:#f9f6f0;
  --white:#ffffff;
  --ink:#1f2a24;
  --muted:#5d625d;
  --sage:#8b9d80;
  --sage-light:#dfe5d8;
  --line:#e4ddd2;
}
*{box-sizing:border-box;margin:0;padding:0}
html,body{width:1200px;height:4539px;overflow:hidden}
body{font-family:"DM Sans",sans-serif;color:var(--ink);background:var(--sand);position:relative}
.serif{font-family:"Playfair Display",serif;font-weight:400}
.abs{position:absolute}
.eyebrow{font-size:9px;letter-spacing:1.6px;font-weight:700;text-transform:uppercase;color:var(--forest-2)}
.divider{position:absolute;width:64px;height:1px;background:var(--rust)}
.divider::after{content:"";position:absolute;left:29px;top:-3px;width:6px;height:6px;background:var(--rust);transform:rotate(45deg)}
.btn{position:absolute;display:flex;align-items:center;justify-content:center;font-size:9.5px;font-weight:700;letter-spacing:1.2px;text-transform:uppercase}

/* nav */
.site-nav{position:absolute;top:0;left:0;width:1200px;height:67px;border-bottom:1px solid rgba(255,255,255,.18);z-index:5}
.brand{position:absolute;left:62px;top:22px;display:flex;align-items:center;gap:10px;color:var(--white)}
.brand-mark{width:14px;height:14px;border:1.5px solid var(--white);border-radius:50%}
.brand-name{font-family:"Playfair Display",serif;font-size:16px;letter-spacing:.5px}
.nav-links{position:absolute;right:190px;top:27px;display:flex;gap:22px;font-size:11px;color:var(--white)}
.nav-book{left:1030px;top:16px;width:110px;height:34px;border:1px solid rgba(255,255,255,.7);color:var(--white)}

/* hero */
.hero{position:absolute;top:0;left:0;width:1200px;height:722px}
.hero-photo{position:absolute;inset:0;background:linear-gradient(90deg,#15281f 0%,#1f3327 38%,rgba(58,52,40,1) 62%,#4a3a2a 80%,#2b3429 100%)}
.hero-photo::after{content:"";position:absolute;inset:0;background:linear-gradient(180deg,rgba(30,45,40,.55) 0%,rgba(20,30,25,0) 40%,rgba(20,30,25,.35) 100%)}
.hero-edge{position:absolute;left:0;bottom:0;width:1200px;height:40px;background:var(--sand)}
.hero-copy{color:var(--white)}
.hero h1{left:73px;top:226px;font-size:58px;line-height:65px;letter-spacing:-1px}
.hero-sub{left:73px;top:370px;width:440px;font-size:12.5px;line-height:22px}
.btn-primary{background:var(--rust);color:var(--white)}
.btn-ghost{border:1px solid rgba(255,255,255,.8);color:var(--white)}
.hero-facts{left:73px;top:492px;font-size:10.5px;color:var(--white);display:flex;gap:10px}
.hero-rating{left:73px;top:520px;font-size:10.5px;color:var(--white);display:flex;gap:14px;align-items:baseline}
.hero-rating b{font-size:13px}

/* booking */
.booking{position:absolute;left:206px;top:686px;width:786px;height:84px;background:var(--white);box-shadow:0 10px 30px rgba(0,0,0,.12);z-index:4}
.booking-tab{position:absolute;left:333px;top:-16px;width:120px;height:18px;background:var(--white);text-align:center;font-size:8px;letter-spacing:1.5px;font-weight:700;padding-top:5px}
.field{position:absolute;top:22px}
.field .eyebrow{font-size:8px}
.field-box{margin-top:8px;height:24px;border-bottom:1px solid var(--line);font-size:11px;color:var(--muted);display:flex;justify-content:space-between;align-items:center}

/* welcome */
.welcome h2{left:101px;top:940px;font-size:42px;line-height:49px;color:var(--forest)}
.welcome p{left:101px;top:1126px;width:360px;font-size:11.5px;line-height:20px;color:var(--muted)}
.link-arrow{left:101px;top:1230px;font-size:9.5px;font-weight:700;letter-spacing:1.2px;color:var(--forest)}
.photo{position:absolute}
.ph-living{background:linear-gradient(135deg,#5c3d25,#9a6a3e 45%,#c58a4a 60%,#4a3320)}
.ph-fire{background:linear-gradient(160deg,#4a3524,#8c5b33 55%,#d28b3e 75%,#3d2a1c)}
.ph-patio{background:linear-gradient(180deg,#3e5167 0%,#5a5a55 50%,#8a6235 80%,#3d4a2f)}
.ph-house{background:linear-gradient(180deg,#2f3f52 0%,#4a4436 45%,#8a5a30 70%,#3a3326)}

.amenities{position:absolute;left:104px;top:1385px;width:990px;height:146px;display:grid;grid-template-columns:repeat(6,1fr);border:1px solid var(--line);background:var(--cream)}
.amenity{border-right:1px solid var(--line);text-align:center;padding-top:28px}
.amenity:last-child{border-right:0}
.amenity svg{width:24px;height:24px;stroke:var(--forest);fill:none;stroke-width:1.5}
.amenity h4{margin-top:10px;font-size:9.5px;font-weight:700;letter-spacing:.4px;text-transform:uppercase}
.amenity p{margin:5px auto 0;width:120px;font-size:9px;line-height:14px;color:var(--muted)}

/* why */
.why{position:absolute;top:1607px;left:0;width:1200px;height:652px;background:var(--cream)}
.why h2{position:absolute;top:110px;width:1200px;text-align:center;font-size:44px;color:var(--forest)}
.hub{position:absolute;left:440px;top:243px;width:318px;height:318px;border-radius:50%;border:1.5px solid var(--sage-light);background:var(--sand);display:flex;align-items:center;justify-content:center;text-align:center}
.hub-mark{width:14px;height:14px;border-radius:50%;background:var(--rust);margin:0 auto 12px}
.hub-name{font-family:"Playfair Display",serif;font-size:22px;line-height:28px;color:var(--forest)}
.spoke{position:absolute;height:1px;background:var(--sage-light)}
.badge{position:absolute;width:72px;height:72px;border-radius:50%;background:var(--sage);box-shadow:0 0 0 5px var(--sage-light);display:flex;align-items:center;justify-content:center}
.badge svg{width:30px;height:30px;stroke:var(--white);fill:none;stroke-width:1.5}
.reason{position:absolute;width:270px}
.reason h4{font-size:11px;font-weight:700;letter-spacing:.4px;text-transform:uppercase;color:var(--forest)}
.reason p{margin-top:6px;font-size:10.5px;line-height:16px;color:var(--muted)}
.reason.left{text-align:right}

/* district */
.district{position:absolute;top:2259px;left:0;width:1200px;height:410px;background:var(--forest)}
.district h2{left:629px;top:97px;font-size:46px;line-height:52px;color:var(--white)}
.district p{left:629px;top:241px;width:460px;font-size:11px;line-height:21px;color:rgba(255,255,255,.85)}

/* reviews */
.reviews h2{left:101px;top:2800px;font-size:42px;line-height:49px;color:var(--forest)}
.quote-card{position:absolute;left:467px;top:2782px;width:631px;height:173px;background:var(--white);border:1px solid var(--line);padding:44px 46px}
.quote-card blockquote{font-family:"Playfair Display",serif;font-size:17px;line-height:28px;color:var(--ink)}
.quote-foot{margin-top:20px;display:flex;justify-content:space-between;font-size:8.5px;font-weight:700;letter-spacing:1.2px;color:var(--muted)}
.quote-foot span:last-child{color:var(--rust);font-size:11px;letter-spacing:1px}

/* rooms */
.section-title{font-size:42px;line-height:49px;color:var(--forest)}
.room{position:absolute;top:3260px;width:322px;height:294px;background:var(--white)}
.room .photo{left:0;top:0;width:322px;height:220px}
.room h3{position:absolute;left:18px;top:236px;font-family:"Playfair Display",serif;font-weight:400;font-size:16px}
.room p{position:absolute;left:18px;top:260px;font-size:10.5px;color:var(--muted)}

/* explore */
.explore{position:absolute;left:101px;top:3841px;width:997px;height:201px;display:grid;grid-template-columns:repeat(4,1fr);background:var(--white)}
.explore-item{border-right:1px solid var(--line);padding:30px 28px}
.explore-item:last-child{border-right:0}
.explore-item .num{font-size:10px;font-weight:700;color:var(--rust)}
.explore-item h3{margin-top:44px;font-family:"Playfair Display",serif;font-weight:400;font-size:19px}
.explore-item p{margin-top:12px;font-size:10.5px;line-height:19px;color:var(--muted);width:160px}

/* cta */
.cta{position:absolute;top:4132px;left:0;width:1200px;height:255px;background:var(--rust);color:var(--white)}
.cta h2{left:84px;top:80px;font-size:40px}
.cta p{left:84px;top:156px;font-size:11px}
.cta-edge{position:absolute;left:0;bottom:0;width:1200px;height:26px;background:var(--forest)}
.btn-light{background:var(--white);color:var(--forest)}

/* footer */
.footer{position:absolute;top:4387px;left:0;width:1200px;height:152px;background:var(--forest);color:var(--white)}
.footer .brand{left:76px;top:32px}
.footer-tag{left:76px;top:70px;font-size:11px;color:rgba(255,255,255,.8)}
.footer-links{position:absolute;right:76px;top:70px;display:flex;gap:20px;font-size:11px}
.footer-rule{position:absolute;left:0;top:108px;width:1200px;height:1px;background:rgba(255,255,255,.12)}
.footer-copy{position:absolute;top:124px;width:1200px;text-align:center;font-size:9px;color:rgba(255,255,255,.6)}
</style>
</head>
<body>

<header class="site-nav">
  <div class="brand"><span class="brand-mark"></span><span class="brand-name">CEDAR LANTERN RETREAT</span></div>
  <nav class="nav-links"><span>The House</span><span>Amenities</span><span>Gallery</span><span>Explore Bend</span><span>Reviews</span></nav>
  <span class="btn nav-book">Book Direct</span>
</header>

<section class="hero">
  <div class="hero-photo" role="img" aria-label="Photograph of the craftsman-style cedar home at dusk among tall pines, windows glowing warmly"></div>
  <div class="hero-edge"></div>
  <div class="hero-copy">
    <div class="abs eyebrow" style="left:73px;top:202px;color:var(--white)">Bend, Oregon</div>
    <h1 class="abs serif">Your Bend getaway,<br>steps from Tanager.</h1>
    <p class="abs hero-sub">A stylish, comfortable home for making memories in the heart of Central Oregon.</p>
    <span class="btn btn-primary" style="left:73px;top:435px;width:150px;height:37px">Check Availability</span>
    <span class="btn btn-ghost" style="left:232px;top:435px;width:150px;height:37px">Explore the House</span>
    <div class="abs hero-facts"><span>3 Bedrooms</span><span>•</span><span>2 Baths</span><span>•</span><span>Sleeps 6</span><span>•</span><span>Pet Friendly</span></div>
    <div class="abs hero-rating"><b>4.98 ★</b><span>205+ Reviews</span><span>Top 1% of homes</span></div>
  </div>
</section>

<form class="booking">
  <div class="booking-tab">PLAN YOUR STAY</div>
  <div class="field" style="left:34px;width:180px"><div class="eyebrow">Check In</div><div class="field-box"><span>dd/mm/yyyy</span><span>▭</span></div></div>
  <div class="field" style="left:246px;width:180px"><div class="eyebrow">Check Out</div><div class="field-box"><span>dd/mm/yyyy</span><span>▭</span></div></div>
  <div class="field" style="left:458px;width:130px"><div class="eyebrow">Guests</div><div class="field-box"><span>1 guest</span><span>⌄</span></div></div>
  <span class="btn btn-primary" style="left:624px;top:22px;width:150px;height:38px">Check Availability</span>
</form>

<section class="welcome">
  <div class="abs eyebrow" style="left:101px;top:914px">Welcome to Cedar Lantern Retreat</div>
  <h2 class="abs serif">Thoughtful<br>comfort in the<br>perfect location.</h2>
  <div class="divider" style="left:101px;top:1100px"></div>
  <p class="abs">Settle into a beautifully appointed three-bedroom home near Bend's Tanager Quarter. Bright gathering spaces, restful bedrooms and a private backyard make it an easy base for days outside and evenings together.</p>
  <div class="abs link-arrow">DISCOVER THE HOUSE →</div>
  <div class="photo ph-living" style="left:527px;top:863px;width:368px;height:430px" role="img" aria-label="Photograph of the living room with stone fireplace, timber beams and tall windows"></div>
  <div class="photo ph-fire" style="left:902px;top:863px;width:196px;height:212px" role="img" aria-label="Photograph of the fireplace seating area"></div>
  <div class="photo ph-patio" style="left:902px;top:1082px;width:196px;height:211px" role="img" aria-label="Photograph of the covered back patio at dusk"></div>
</section>

<div class="amenities">
  <div class="amenity"><svg viewBox="0 0 24 24"><path d="M12 20s-7-4.5-7-10a4 4 0 0 1 7-2.5A4 4 0 0 1 19 10c0 5.5-7 10-7 10z"/></svg><h4>Pet Friendly</h4><p>Fenced yard and room to relax.</p></div>
  <div class="amenity"><svg viewBox="0 0 24 24"><path d="M12 21s-6-6.5-6-11a6 6 0 0 1 12 0c0 4.5-6 11-6 11z"/><circle cx="12" cy="10" r="2"/></svg><h4>Walk to Tanager</h4><p>Dining, shops and river paths nearby.</p></div>
  <div class="amenity"><svg viewBox="0 0 24 24"><path d="M12 3c1 4 5 6 5 11a5 5 0 0 1-10 0c0-3 2-4 2-6 2 1 3 3 3 3s1-4 0-8z"/></svg><h4>Outdoor Living</h4><p>Covered patio and fire-pit table.</p></div>
  <div class="amenity"><svg viewBox="0 0 24 24"><circle cx="10" cy="10" r="3.5"/><path d="M10 2v3M10 15v3M2 10h3M15 10h3M4.5 4.5l2 2M13.5 13.5l2 2M15.5 4.5l-2 2M4.5 15.5l2-2M18 16v6M16 18h4"/></svg><h4>Year-Round Comfort</h4><p>Fireplace, heating and air conditioning.</p></div>
  <div class="amenity"><svg viewBox="0 0 24 24"><path d="M3 9a13 13 0 0 1 18 0M6 12.5a8.5 8.5 0 0 1 12 0M9 16a4 4 0 0 1 6 0"/><circle cx="12" cy="19" r="1"/></svg><h4>Fast Wi-Fi</h4><p>Reliable connection throughout.</p></div>
  <div class="amenity"><svg viewBox="0 0 24 24"><path d="M4 16V12l2-5h12l2 5v4z"/><path d="M4 12h16"/><circle cx="7.5" cy="14" r=".8"/><circle cx="16.5" cy="14" r=".8"/><path d="M6 16v2M18 16v2"/></svg><h4>Easy Parking</h4><p>Dedicated off-street driveway.</p></div>
</div>

<section class="why">
  <div class="eyebrow" style="position:absolute;top:95px;width:1200px;text-align:center">A Stay Designed Around You</div>
  <h2 class="serif">Why Guests Choose Cedar Lantern Retreat</h2>
  <div class="divider" style="left:568px;top:187px"></div>

  <div class="spoke" style="left:418px;top:287px;width:70px;transform:rotate(6deg)"></div>
  <div class="spoke" style="left:418px;top:402px;width:24px"></div>
  <div class="spoke" style="left:418px;top:512px;width:70px;transform:rotate(-6deg)"></div>
  <div class="spoke" style="left:710px;top:287px;width:70px;transform:rotate(-6deg)"></div>
  <div class="spoke" style="left:756px;top:402px;width:24px"></div>
  <div class="spoke" style="left:710px;top:512px;width:70px;transform:rotate(6deg)"></div>

  <div class="hub"><div><div class="hub-mark"></div><div class="hub-name">Cedar Lantern<br>Retreat</div></div></div>

  <div class="badge" style="left:346px;top:235px"><svg viewBox="0 0 24 24"><path d="M12 21s-6-6.5-6-11a6 6 0 0 1 12 0c0 4.5-6 11-6 11z"/><circle cx="12" cy="10" r="2"/></svg></div>
  <div class="badge" style="left:346px;top:346px"><svg viewBox="0 0 24 24"><circle cx="12" cy="12" r="9"/><path d="M12 7l1.5 3.2 3.5.4-2.6 2.3.8 3.4L12 14.6 8.8 16.3l.8-3.4L7 10.6l3.5-.4z"/></svg></div>
  <div class="badge" style="left:346px;top:457px"><svg viewBox="0 0 24 24"><path d="M12 20s-7-4.5-7-10a4 4 0 0 1 7-2.5A4 4 0 0 1 19 10c0 5.5-7 10-7 10z"/></svg></div>
  <div class="badge" style="left:776px;top:235px"><svg viewBox="0 0 24 24"><path d="M4 18V11h16v7M4 14h16M6 11V7h12v4M3 18h18"/></svg></div>
  <div class="badge" style="left:776px;top:346px"><svg viewBox="0 0 24 24"><rect x="5" y="4" width="14" height="16"/><path d="M8 16h8M9 12l3-4 3 4z"/></svg></div>
  <div class="badge" style="left:776px;top:457px"><svg viewBox="0 0 24 24"><rect x="4" y="5" width="16" height="15"/><path d="M4 9h16M8 3v4M16 3v4M8 13h2M12 13h2M8 16h2"/></svg></div>

  <div class="reason left" style="left:54px;top:264px"><h4>Walk to Tanager</h4><p>Restaurants, shops and river paths are just minutes away.</p></div>
  <div class="reason left" style="left:54px;top:375px"><h4>Exceptional Guest Rating</h4><p>Rated 4.98 with 200+ reviews and ranked among the Top 1%.</p></div>
  <div class="reason left" style="left:54px;top:486px"><h4>Pet-Friendly Stay</h4><p>A private fenced backyard gives pets room to relax safely.</p></div>
  <div class="reason" style="left:876px;top:264px"><h4>Comfortable for Six</h4><p>Three inviting bedrooms and two bathrooms for families and friends.</p></div>
  <div class="reason" style="left:876px;top:375px"><h4>Thoughtful Amenities</h4><p>A well-equipped kitchen, fireplace, fast Wi-Fi and convenient parking.</p></div>
  <div class="reason" style="left:876px;top:486px"><h4>Book Direct with Confidence</h4><p>Check availability, view complete pricing and reserve securely online.</p></div>
</section>

<section class="district">
  <div class="photo ph-house" style="left:0;top:0;width:546px;height:410px" role="img" aria-label="Photograph of the home's front exterior at twilight with lit windows and stone chimney"></div>
  <div class="abs eyebrow" style="left:629px;top:76px;color:var(--white)">The Best of Bend, Close By</div>
  <h2 class="abs serif">A short walk to the<br>Tanager Quarter.</h2>
  <div class="divider" style="left:629px;top:213px"></div>
  <p class="abs">Follow the Kettleback River, catch a show at Brightwater Lawn Pavilion, browse local shops or choose a table at one of Bend's favorite restaurants.</p>
  <span class="btn btn-ghost" style="left:629px;top:305px;width:118px;height:36px;font-size:9px">Explore Bend</span>
</section>

<section class="reviews">
  <div class="abs eyebrow" style="left:101px;top:2762px">Guest Love</div>
  <h2 class="abs serif">What our<br>guests are<br>saying</h2>
  <div class="divider" style="left:101px;top:2950px"></div>
  <div class="quote-card">
    <blockquote>“Perfect location, beautiful home and thoughtful details. We walked to Tanager and loved relaxing by the backyard fire.”</blockquote>
    <div class="quote-foot"><span>RECENT GUEST REVIEW</span><span>★★★★★</span></div>
  </div>
</section>

<section class="rooms">
  <div class="abs eyebrow" style="left:101px;top:3083px">Rooms &amp; Spaces</div>
  <h2 class="abs serif section-title" style="left:101px;top:3112px">Room to rest, gather and<br>recharge.</h2>
  <div class="divider" style="left:101px;top:3220px"></div>
  <article class="room" style="left:100px"><div class="photo ph-living" role="img" aria-label="Photograph of the primary suite lounge with fireplace"></div><h3>Primary Suite</h3><p>King bed · restful retreat</p></article>
  <article class="room" style="left:439px"><div class="photo ph-patio" role="img" aria-label="Photograph of the guest wing and covered patio"></div><h3>Guest Bedroom</h3><p>Queen bed · soft natural light</p></article>
  <article class="room" style="left:777px"><div class="photo ph-house" role="img" aria-label="Photograph of the home exterior at dusk"></div><h3>Third Bedroom</h3><p>Comfortable space for two</p></article>
</section>

<section class="explore-wrap">
  <div class="abs eyebrow" style="left:101px;top:3664px">Explore Bend</div>
  <h2 class="abs serif section-title" style="left:101px;top:3692px">Adventure begins at your<br>doorstep.</h2>
  <div class="divider" style="left:101px;top:3800px"></div>
  <div class="explore">
    <div class="explore-item"><div class="num">01</div><h3>River &amp; trails</h3><p>Walk, paddle or bike along the Kettleback.</p></div>
    <div class="explore-item"><div class="num">02</div><h3>Food &amp; breweries</h3><p>Discover Bend's relaxed local flavor.</p></div>
    <div class="explore-item"><div class="num">03</div><h3>Live music</h3><p>Summer nights at the pavilion.</p></div>
    <div class="explore-item"><div class="num">04</div><h3>Mountain days</h3><p>Easy access to Central Oregon scenery.</p></div>
  </div>
</section>

<section class="cta">
  <div class="abs eyebrow" style="left:84px;top:56px;color:var(--white)">Plan Your Stay</div>
  <h2 class="abs serif">Ready for your Bend getaway?</h2>
  <p class="abs">Book direct for a simple, personal reservation experience.</p>
  <span class="btn btn-light" style="left:967px;top:93px;width:148px;height:39px">Check Availability</span>
  <div class="cta-edge"></div>
</section>

<footer class="footer">
  <div class="brand"><span class="brand-mark"></span><span class="brand-name">CEDAR LANTERN RETREAT</span></div>
  <div class="abs footer-tag">Your welcoming home base in Bend, Oregon.</div>
  <nav class="footer-links"><span>The House</span><span>Explore Bend</span><span>Reviews</span><span>Contact</span></nav>
  <div class="footer-rule"></div>
  <div class="footer-copy">© 2026 Cedar Lantern Retreat. All rights reserved.</div>
</footer>

</body>
</html>
```